Bref créative
Dunmore Corner Mart -Business Card
Professional
Dunmore Corner Mart
284 North Elmridge,
Salem, NH 03079
dunmorecornermart@mailbox-example.com
We do not have the number yet, but we will soon. Please use 0's until we have an actual one. We need different variations of business cards. One to focus on cigars, one on wine and other on market itself which is to include supermarket goods. Our slogan needs to be 'More bang for your buck!'
One will have all items: Cigars, Wine, Beer, Cigarettes, Tobacco, Groceries,
Others will have the focus points and accessories. (I.e. Cigar one will have Cigars, Cigar Accessories, Lighters, Cigar cutters etc). We will be providing details very soon
We need same type for wine also. Details to follow

```html
<!DOCTYPE html>
<html lang="en">
<head>
<meta charset="utf-8">
<title>Dunmore Corner Mart – Stationery Set</title>
<link rel="stylesheet" href="https://fonts.googleapis.com/css2?family=Roboto+Slab:wght@700&family=Open+Sans:wght@400;600&display=swap">
<style>
  :root{
    --backdrop:#5b3e2b;
    --paper:#ffffff;
    --paper-shade:#f1efec;
    --brand-red:#a5212a;
    --brand-red-dark:#7e161d;
    --brand-brown:#9b6b3c;
    --ink:#4a3b34;
    --label:#e8d9c8;
    --faint:rgba(165,33,42,.08);
  }
  *{box-sizing:border-box;margin:0;padding:0}
  html,body{width:1200px;height:439px;overflow:hidden}
  body{background:var(--backdrop);font-family:"Open Sans",sans-serif;color:var(--ink);position:relative}
  .piece{position:absolute;background:var(--paper);box-shadow:0 2px 6px rgba(0,0,0,.35)}
  .brand-name{font-family:"Roboto Slab",serif;font-weight:700;color:var(--brand-red);text-transform:uppercase;letter-spacing:.5px;white-space:nowrap}
  .brand-mark{display:flex;align-items:center;gap:4px}
  .brand-dot{width:9px;height:9px;border-radius:50%;background:var(--brand-red);flex:none}
  .band{position:absolute;left:0;right:0;background:var(--brand-red)}
  .small{font-size:5px;line-height:7px}
  .label{position:absolute;font-size:7px;color:var(--label);text-align:center}

  /* business cards */
  .card{left:24px;width:164px}
  .card-front{top:53px;height:96px}
  .card-slogan{top:180px;height:89px}
  .card-list{top:283px;height:101px}
  .card-front .band{top:22px;height:14px}
  .card-front .brand-mark{position:absolute;left:10px;top:10px;background:var(--paper);padding:4px 6px;border:1px solid var(--brand-red)}
  .card-front .brand-name{font-size:7px}
  .card-front .contact{position:absolute;left:12px;top:46px}
  .card-front .contact-right{position:absolute;left:84px;top:46px}
  .card-slogan .brand-mark{position:absolute;left:50%;top:22px;transform:translateX(-50%)}
  .card-slogan .brand-name{font-size:8px}
  .card-slogan .slogan{position:absolute;left:0;right:0;top:52px;text-align:center;font-size:6px;font-weight:600;color:var(--brand-red)}
  .card-list .brand-mark{position:absolute;left:10px;top:38px;width:86px}
  .card-list .brand-name{font-size:7px;line-height:10px;white-space:normal}
  .card-list ul{position:absolute;left:112px;top:16px;list-style:none}
  .card-list li{font-size:5.5px;line-height:11px}
  .card-list li::before{content:"";display:inline-block;width:3px;height:3px;background:var(--brand-red);margin-right:4px;vertical-align:middle}

  /* letterheads */
  .letter{top:24px;width:288px;height:372px}
  .letter-one{left:204px}
  .letter-two{left:504px}
  .letter .band{top:17px;height:13px}
  .letter .brand-mark{position:absolute;left:16px;top:10px;background:var(--paper);padding:5px 8px;border:1px solid var(--brand-red)}
  .letter .brand-name{font-size:8px}
  .letter .header-contact{position:absolute;right:12px;top:3px;text-align:right;color:var(--ink);line-height:6px}
  .letter .watermark{position:absolute;left:0;right:0;top:160px;text-align:center;font-family:"Roboto Slab",serif;font-weight:700;font-size:18px;white-space:nowrap;color:var(--faint);text-transform:uppercase}
  .letter .footer-contact{position:absolute;left:0;right:0;bottom:10px;text-align:center}
  .letter-two .band{top:auto;bottom:24px;height:3px}

  /* envelopes */
  .envelope{left:828px;width:348px;height:108px}
  .env-red{top:24px;background:var(--paper-shade)}
  .env-brown{top:84px;background:var(--paper-shade)}
  .env-open{top:192px}
  .env-front{top:264px;height:108px}
  .flap{position:absolute;left:0;top:0;width:100%;height:100%}
  .envelope .brand-mark{position:absolute;left:50%;top:44px;transform:translateX(-50%);background:var(--paper);padding:3px 6px}
  .envelope .brand-name{font-size:7px}
  .env-front .band{top:46px;height:16px}
  .env-front .brand-mark{left:14px;top:38px;transform:none;border:1px solid var(--brand-red)}
  .env-front .return-address{position:absolute;left:16px;top:68px}
</style>
</head>
<body>

<!-- business cards -->
<section class="piece card card-front">
  <div class="band"></div>
  <div class="brand-mark"><span class="brand-dot"></span><span class="brand-name">Dunmore Corner Mart</span></div>
  <div class="contact small">
    <strong>Owner Name</strong><br>Store Manager<br>284 North Elmridge,<br>Salem, NH 03079
  </div>
  <div class="contact-right small">
    Tel: 000 000 0000<br>jkowal@mailbox-example.com<br>dunmorecornermart@<br>mailbox-example.com
  </div>
</section>
<div class="label" style="left:24px;top:153px;width:164px">Business Cards</div>

<section class="piece card card-slogan">
  <div class="brand-mark"><span class="brand-dot"></span><span class="brand-name">Dunmore Corner Mart</span></div>
  <p class="slogan">More bang for your buck!</p>
</section>

<section class="piece card card-list">
  <div class="brand-mark"><span class="brand-dot"></span><span class="brand-name">Dunmore Corner Mart</span></div>
  <ul>
    <li>Cigars</li><li>Wine</li><li>Beer</li><li>Cigarettes</li><li>Tobacco</li><li>Groceries</li>
  </ul>
</section>

<!-- letterheads -->
<section class="piece letter letter-one">
  <div class="band"></div>
  <div class="brand-mark"><span class="brand-dot"></span><span class="brand-name">Dunmore Corner Mart</span></div>
  <div class="header-contact small">284 North Elmridge, Salem, NH 03079<br>Tel: 000 000 0000</div>
  <div class="watermark">Dunmore Corner Mart</div>
</section>
<div class="label" style="left:204px;top:400px;width:288px">Letterhead Front</div>

<section class="piece letter letter-two">
  <div class="band"></div>
  <div class="watermark">Dunmore Corner Mart</div>
  <div class="footer-contact small">284 North Elmridge, Salem, NH 03079 · dunmorecornermart@mailbox-example.com</div>
</section>
<div class="label" style="left:504px;top:400px;width:288px">Letterhead Back</div>

<!-- envelopes -->
<section class="piece envelope env-red">
  <svg class="flap" viewBox="0 0 348 108" preserveAspectRatio="none"><polygon points="0,0 348,0 174,80" fill="var(--brand-red)"/></svg>
  <div class="brand-mark"><span class="brand-dot"></span><span class="brand-name">Dunmore Corner Mart</span></div>
</section>
<section class="piece envelope env-brown">
  <svg class="flap" viewBox="0 0 348 108" preserveAspectRatio="none"><polygon points="0,0 348,0 174,80" fill="var(--brand-brown)"/></svg>
  <div class="brand-mark"><span class="brand-dot"></span><span class="brand-name">Dunmore Corner Mart</span></div>
</section>
<section class="piece envelope env-open">
  <svg class="flap" viewBox="0 0 348 108" preserveAspectRatio="none"><polyline points="0,0 174,70 348,0" fill="none" stroke="#ddd" stroke-width="1.5"/></svg>
  <div class="brand-mark"><span class="brand-dot"></span><span class="brand-name">Dunmore Corner Mart</span></div>
</section>
<section class="piece envelope env-front">
  <div class="band"></div>
  <div class="brand-mark"><span class="brand-dot"></span><span class="brand-name">Dunmore Corner Mart</span></div>
  <div class="return-address small">284 North Elmridge, Salem, NH 03079</div>
</section>
<div class="label" style="left:828px;top:378px;width:348px">Envelope Set</div>

</body>
</html>
```